Online Nutrition Consulting Website/healthy lifestyle

This is a website for online nutrition consulting. (For example, weight loss.) The company is called Mirela's. I included the logo so you have a feel for the colors and the message of the company. I would like to have one main neutral color in there. (I am leaning toward grey, but I am open to ideas) I would like the design to be simple and to the point.

My ultimate goal is for my website to stand out from other nutrition websites by projecting my slogan (It's not a diet. It's a lifestyle.)

Target Market(s)

Health-conscious people.

Industry/Entity Type

Nutrition

Coding

Coded - Design and coding required

Number of Pages Required

4 page

Font styles to use
Script

Requirements
Must have
• Home page, Services page , About page, and a Blog page. (Once I see the layout, I will give you more detail so it isn't confusing. For example: payment of services and the "About me")
• Logo must be included.
• Easy navigation. Not too much scrolling.

```html
<!DOCTYPE html>
<html lang="en">
<head>
<meta charset="utf-8">
<title>Mirela's – Online Nutrition Consulting</title>
<link href="https://fonts.googleapis.com/css2?family=Open+Sans:wght@300;400;600;700&display=swap" rel="stylesheet">
<style>
:root{
  --blue:#1ba6df;
  --blue-dark:#0f86c0;
  --green:#8cc63e;
  --green-dark:#74ad2c;
  --ink:#3a3a3a;
  --muted:#777;
  --panel:#ededed;
  --panel-edge:#dcdcdc;
  --dark:#1c1c1c;
  --darker:#121212;
  --white:#fff;
}
*{box-sizing:border-box;margin:0;padding:0}
html,body{width:1200px;height:3076px;overflow:hidden}
body{font-family:"Open Sans",Arial,sans-serif;color:var(--ink);background:var(--white);position:relative}
section,header,footer{position:absolute;left:0;width:1200px}
.btn{display:inline-block;background:var(--green);color:var(--white);font-weight:600;font-size:17px;padding:8px 24px;border-radius:20px;text-transform:uppercase;letter-spacing:.5px}
.lead{font-size:15px;line-height:1.6;color:var(--muted)}
.on-blue{color:#e8f6fd}

/* header */
.site-header{top:0;height:160px;background:var(--white)}
.brand{position:absolute;left:84px;top:50px}
.brand-name{font-size:44px;font-weight:600;color:var(--blue);line-height:1}
.main-nav{position:absolute;right:80px;top:62px;display:flex;gap:14px}
.main-nav a{font-size:19px;color:var(--green-dark);padding:10px 22px;border-radius:24px;text-decoration:none;text-transform:uppercase}
.main-nav a.active{background:var(--green);color:var(--white)}

/* hero */
.hero{top:160px;height:420px;background:linear-gradient(90deg,#e9f4fa 0%,#b7e0f3 30%,var(--blue) 55%,var(--blue-dark) 100%)}
.hero-photo{position:absolute;left:0;top:0;width:620px;height:420px;background:linear-gradient(90deg,#dcebf3,#f4d6c4 45%,#bfe3f4)}
.hero-copy{position:absolute;left:716px;top:70px;color:var(--white)}
.hero-copy h1{font-weight:400;font-size:48px;line-height:1.12;text-transform:uppercase}
.hero-copy h2{font-weight:400;font-size:28px;margin-top:18px}
.hero-copy p{font-size:15px;line-height:1.55;width:400px;margin-top:6px;color:#e8f6fd}
.hero-copy .btn{margin-top:28px}

/* welcome */
.welcome{top:580px;height:280px;text-align:center}
.welcome h2{font-weight:400;font-size:48px;color:var(--blue);margin-top:42px}
.welcome h2 span{color:var(--green)}
.welcome p{width:720px;margin:28px auto 0}

/* band headings */
.band{background:linear-gradient(180deg,var(--blue),var(--blue-dark))}
.band h2{position:absolute;left:0;width:1200px;text-align:center;font-weight:300;font-size:60px;color:var(--white)}
.band p{position:absolute;left:0;width:1200px;text-align:center;font-size:15px;line-height:1.6}
.service-band{top:860px;height:200px}
.service-band h2{top:30px}
.service-band p{top:118px}
.band-figure{position:absolute;border-radius:6px}
.service-figure{left:975px;top:-60px;width:190px;height:260px;background:linear-gradient(180deg,#f3ddd0,#e7a9b9 60%,#2f9fd6)}

/* service cards */
.services{top:1060px;height:480px;background:#f6f6f6}
.services .panel{position:absolute;left:80px;top:0;width:1040px;height:460px;background:var(--panel);border:1px solid var(--panel-edge);border-radius:0 0 22px 22px}
.service-item{position:absolute;top:64px;width:300px;text-align:center}
.service-item .thumb{width:164px;height:164px;border-radius:50%;margin:0 auto;border:5px solid var(--white);box-shadow:0 0 0 2px #cfe8c0}
.service-item h3{font-weight:400;font-size:25px;color:var(--blue);margin-top:16px}
.service-item p{font-size:14px;line-height:1.55;color:var(--muted);margin-top:14px;padding:0 14px}
.service-item .btn{margin-top:28px}

/* testimonial */
.testimonial{top:1540px;height:500px;background:linear-gradient(90deg,#2a2a2a,#5b5148 45%,#4a4f36 75%,#2c2c2c)}
.testimonial h2{position:absolute;top:56px;width:1200px;text-align:center;font-weight:400;font-size:48px;color:var(--white)}
.testimonial p{position:absolute;top:136px;left:250px;width:700px;text-align:center;font-size:15px;line-height:1.6;color:#e4e4e4}
.client-name{position:absolute;top:238px;width:1200px;text-align:center;font-size:13px;font-weight:700;color:var(--white);letter-spacing:1px}
.client-photo{position:absolute;left:530px;top:300px;width:150px;height:150px;border-radius:50%;border:5px solid var(--white);background:linear-gradient(160deg,#f2d9cc,#d9a995)}
.arrow{position:absolute;top:228px}
.arrow-left{left:78px}
.arrow-right{right:78px}

/* blog */
.blog-band{top:2040px;height:200px}
.blog-band h2{top:20px}
.blog-band p{top:100px}
.blog-figure{left:870px;top:-80px;width:300px;height:300px;background:linear-gradient(180deg,#f0c9bf,#d64a8c 55%,#e9c53a)}
.blog{top:2240px;height:340px;background:#f6f6f6}
.blog .panel{position:absolute;left:80px;top:0;width:1040px;height:320px;background:var(--panel);border:1px solid var(--panel-edge);border-radius:0 0 22px 22px}
.post{position:absolute;top:48px;width:286px}
.post .thumb{width:286px;height:144px;position:relative}
.post .caption{position:absolute;left:0;bottom:0;width:100%;height:22px;background:var(--blue);color:var(--white);font-size:11px;line-height:22px;padding-left:8px}
.post h3{font-weight:400;font-size:22px;color:var(--blue);margin-top:18px}
.post p{font-size:14px;line-height:1.5;color:var(--muted);margin-top:4px}

/* newsletter */
.newsletter{top:2580px;height:240px;background:linear-gradient(180deg,var(--green),var(--green-dark));text-align:center}
.newsletter h2{font-weight:400;font-size:48px;color:var(--white);margin-top:40px}
.newsletter p{font-size:14px;color:#f1f9e6;margin-top:2px}
.signup{position:absolute;left:160px;top:148px;display:flex;gap:22px;align-items:center}
.field{width:276px;height:40px;border:1px solid var(--white);background:rgba(255,255,255,.12);color:var(--white);font-size:13px;line-height:38px;text-align:left;padding-left:14px}
.signup .btn{background:var(--blue);text-transform:none;font-size:17px;padding:8px 24px;margin-left:76px}

/* footer */
.site-footer{top:2820px;height:256px;background:var(--dark)}
.footer-nav{position:absolute;left:80px;top:36px;display:flex;gap:30px;align-items:center}
.footer-nav a{color:#ddd;font-size:17px;text-decoration:none}
.footer-nav a.active{border:1px solid var(--green);color:var(--green);border-radius:20px;padding:6px 18px}
.social{position:absolute;right:90px;top:46px;display:flex;gap:40px}
.social span{width:22px;height:22px;border-radius:50%;background:var(--blue)}
.footer-rule{position:absolute;left:80px;top:110px;width:1040px;height:1px;background:#333}
.footer-bottom{position:absolute;left:0;top:130px;width:1200px;height:126px;background:var(--darker)}
.contact h3{position:absolute;left:80px;top:16px;font-size:23px;font-weight:400;color:var(--white)}
.contact-item{position:absolute;top:50px;display:flex;gap:12px;font-size:14px;color:#ccc;line-height:1.5}
.contact-item .icon{width:34px;height:34px;border-radius:50%;background:#2e2e2e;flex:none;display:flex;align-items:center;justify-content:center}
.copyright{position:absolute;right:80px;top:56px;font-size:13px;color:#aaa}
.copyright b{color:var(--green);font-weight:600}
</style>
</head>
<body>

<header class="site-header">
  <div class="brand"><span class="brand-name">Mirela's</span></div>
  <nav class="main-nav">
    <a class="active" href="#">Home</a><a href="#">About</a><a href="#">Services</a><a href="#">Blog</a><a href="#">Contact</a>
  </nav>
</header>

<section class="hero">
  <div class="hero-photo" role="img" aria-label="Photo of a slim woman measuring her waist with a yellow tape measure"></div>
  <div class="hero-copy">
    <h1>It's not a diet.<br>It's a lifestyle</h1>
    <h2>With our Help</h2>
    <p>Lorem ipsum is simply dummy text of the printing and typesetting industry.</p>
    <span class="btn">Read more</span>
  </div>
</section>

<section class="welcome">
  <h2>Welcome to <span>Mirela's</span></h2>
  <p class="lead">Lorem ipsum is simply dummy text of the printing and typesetting industry. Lorem Ipsum has been the industry's standard dummy text ever since the 1500s, when an unknown printer took a galley of type and scrambled it to make a type specimen book. It has survived not only five centuries.</p>
</section>

<section class="band service-band">
  <div class="band-figure service-figure" role="img" aria-label="Photo of a smiling woman in sportswear holding a water bottle"></div>
  <h2>Service</h2>
  <p class="on-blue">Lorem ipsum is simply dummy text of the printing and<br>typesetting industry. Lorem Ipsum has been.</p>
</section>

<section class="services">
  <div class="panel">
    <div class="service-item" style="left:20px">
      <div class="thumb" role="img" aria-label="Photo of a woman with glowing skin" style="background:linear-gradient(160deg,#f5e0d3,#d9b09a)"></div>
      <h3>Gorgeous Skin</h3>
      <p>Lorem ipsum is simply dummy text of the printing and typesetting industry. Lorem Ipsum has been the industry.</p>
      <span class="btn">Read more</span>
    </div>
    <div class="service-item" style="left:370px">
      <div class="thumb" role="img" aria-label="Photo of a waist with a measuring tape" style="background:linear-gradient(160deg,#f7efe9,#e6c8b6)"></div>
      <h3>Weight Management</h3>
      <p>Lorem ipsum is simply dummy text of the printing and typesetting industry. Lorem Ipsum has been the industry.</p>
      <span class="btn">Read more</span>
    </div>
    <div class="service-item" style="left:720px">
      <div class="thumb" role="img" aria-label="Photo of a woman outdoors with fresh fruit" style="background:linear-gradient(160deg,#bfe0ef,#9ccd6a)"></div>
      <h3>Health Tips</h3>
      <p>Lorem ipsum is simply dummy text of the printing and typesetting industry. Lorem Ipsum has been the industry.</p>
      <span class="btn">Read more</span>
    </div>
  </div>
</section>

<section class="testimonial" role="img" aria-label="Dark background photo of fresh vegetables and fruit">
  <h2>What Our Client Say</h2>
  <p>Lorem ipsum is simply dummy text of the printing and typesetting industry. Lorem Ipsum has been the industry's standard dummy text ever since the 1500s, when an unknown printer took a galley of type and scrambled it to make a type specimen book. It has survived not only five centuries.</p>
  <div class="client-name">- CLIENT NAME</div>
  <div class="client-photo" role="img" aria-label="Portrait of a happy client"></div>
  <svg class="arrow arrow-left" width="24" height="44" viewBox="0 0 24 44"><path d="M20 2 L4 22 L20 42" fill="none" stroke="#fff" stroke-width="3"/></svg>
  <svg class="arrow arrow-right" width="24" height="44" viewBox="0 0 24 44"><path d="M4 2 L20 22 L4 42" fill="none" stroke="#fff" stroke-width="3"/></svg>
</section>

<section class="band blog-band">
  <div class="band-figure blog-figure" role="img" aria-label="Photo of a fit woman with dumbbell, apple and measuring tape"></div>
  <h2>Blog</h2>
  <p class="on-blue">Lorem ipsum is simply dummy text of the printing and<br>typesetting industry. Lorem Ipsum has been.</p>
</section>

<section class="blog">
  <div class="panel">
    <article class="post" style="left:40px">
      <div class="thumb" role="img" aria-label="Photo of a woman with a basket of fresh vegetables" style="background:linear-gradient(120deg,#e8b24a,#f3e3d6 55%,#9cc35a)"><span class="caption">Posted on 12 May 2015 by Admin</span></div>
      <h3>Blog Title</h3>
      <p>Lorem ipsum is simply dummy text of the printing and typesetting industry.</p>
    </article>
    <article class="post" style="left:376px">
      <div class="thumb" role="img" aria-label="Photo of a bowl of mixed fresh fruit" style="background:linear-gradient(120deg,#7fb34a,#e6483a 50%,#f3c04a)"><span class="caption">Posted on 12 May 2015 by Admin</span></div>
      <h3>Blog Title</h3>
      <p>Lorem ipsum is simply dummy text of the printing and typesetting industry.</p>
    </article>
    <article class="post" style="left:712px">
      <div class="thumb" role="img" aria-label="Photo of a woman measuring her waist" style="background:linear-gradient(120deg,#f6ebe3,#e2b7a2 55%,#f4f0ec)"><span class="caption">Posted on 12 May 2015 by Admin</span></div>
      <h3>Blog Title</h3>
      <p>Lorem ipsum is simply dummy text of the printing and typesetting industry.</p>
    </article>
  </div>
</section>

<section class="newsletter">
  <h2>Newsletter</h2>
  <p>Lorem ipsum is simply dummy text of the printing and typesetting industry.</p>
  <div class="signup">
    <div class="field">Enter Name</div>
    <div class="field">Enter Email</div>
    <span class="btn">Subscribe</span>
  </div>
</section>

<footer class="site-footer">
  <nav class="footer-nav">
    <a class="active" href="#">Home</a><a href="#">About</a><a href="#">Services</a><a href="#">Blog</a><a href="#">Contact</a>
  </nav>
  <div class="social"><span></span><span></span><span></span></div>
  <div class="footer-rule"></div>
  <div class="footer-bottom contact">
    <h3>Contact Us</h3>
    <div class="contact-item" style="left:80px">
      <span class="icon"><svg width="14" height="18" viewBox="0 0 14 18"><path d="M7 1a6 6 0 0 0-6 6c0 4.5 6 10 6 10s6-5.5 6-10a6 6 0 0 0-6-6z" fill="#8cc63e"/><circle cx="7" cy="7" r="2.2" fill="#2e2e2e"/></svg></span>
      <span>Lorem ipsum is simply dummy<br>text of the printing and<br>typesetting industry.</span>
    </div>
    <div class="contact-item" style="left:360px;top:58px">
      <span class="icon"><svg width="16" height="16" viewBox="0 0 16 16"><path d="M3 1l3 3-2 2c1 2 3 4 5 5l2-2 3 3-2 2C7 14 2 9 1 3z" fill="#8cc63e"/></svg></span>
      <span style="line-height:34px">Call : 123 456 789</span>
    </div>
    <div class="contact-item" style="left:580px;top:58px">
      <span class="icon"><svg width="16" height="16" viewBox="0 0 16 16"><rect x="2" y="6" width="12" height="8" fill="#8cc63e"/><rect x="4" y="2" width="8" height="5" fill="none" stroke="#8cc63e" stroke-width="1.5"/></svg></span>
      <span style="line-height:34px">Fax : 123 456 789</span>
    </div>
    <div class="copyright"><b>© Mirela's</b> - 2015. All Rights Reserved.</div>
  </div>
</footer>

</body>
</html>
```